Indie musician needs album cover art

I am an independant musician releasing my second album via digital sources. I plan to make it available on Songvault and other digital stores but primarily distribute it free through Tunebarn.

The album's music style is a blend of singer-songwriter folk, punk, alt country, electronic rock and spoken word. The lyrical content is a dark journey through travel in foreign countries, relationships, airports and theatres, formed during my own journey as an audio engineer for a travelling theatre show.

The album is called "Lo Find Quiet" - at times both a plea and a directive. I would like the album cover to reflect a sense of longing, restlessness, unease and movement. A subversive tone is also possible.

I have had a go at designing a couple of ideas myself, using my own photos. I like the ideas but I am not skilled in graphic design and am unable to take them further to get the right feel and look. I will post these as examples of tone. The finished work does not need to copy either of these.

A .zip of the album can be downloaded here (low fi mp3):

http://qlnk.example/Xr7tP4

Target Market(s)

People who enjoy thoughtful, honest, homemade music. Definitely not a teeny pop audience. Adult, subversive, educated, emotional...

Industry/Entity Type

Graphic Design

Requirements
Must have
• Artist name (no caps): kestrin
Album name (prefer no caps): lo find quiet

```html
<!DOCTYPE html>
<html lang="en">
<head>
<meta charset="utf-8">
<title>kestrin — lo find quiet</title>
<link rel="stylesheet" href="https://fonts.googleapis.com/css2?family=Cormorant+Garamond:wght@300;400&display=swap">
<style>
  :root {
    --page: #ffffff;
    --sleeve: #050505;
    --type: #a6a6a6;
    --night-deep: #070806;
    --night-mid: #2a2a18;
    --haze: #6e6e3c;
    --lamp: #e2d27a;
    --crowd: #5a4a3a;
    --balloon: #b0587e;
    --ground: #1c1c12;
    --glow-pale: #eef9d2;
    --glow-green: #9cd838;
    --glow-mid: #5e8a1c;
    --glow-deep: #24360a;
    --reflect: #b0b0b0;
  }
  * { margin: 0; padding: 0; box-sizing: border-box; }
  html, body { width: 1200px; height: 900px; overflow: hidden; background: var(--page); }
  .stage { position: relative; width: 1200px; height: 900px; }

  .cover { position: absolute; background: var(--sleeve); overflow: hidden; }
  .cover--festival { left: 30px; top: 240px; width: 550px; height: 548px; }
  .cover--house { left: 624px; top: 240px; width: 552px; height: 550px; }

  .festival-photo {
    position: absolute; inset: 0;
    background:
      radial-gradient(ellipse 90% 80% at 45% 50%, transparent 45%, rgba(0,0,0,0.85) 100%),
      radial-gradient(circle 40px at 88% 38%, var(--lamp) 0%, rgba(226,210,122,0.35) 45%, transparent 100%),
      radial-gradient(circle 60px at 60% 14%, rgba(226,210,122,0.55) 0%, transparent 100%),
      radial-gradient(ellipse 18% 20% at 30% 68%, var(--balloon) 0%, rgba(176,88,126,0.35) 60%, transparent 100%),
      linear-gradient(168deg, transparent 0%, transparent 42%, rgba(190,190,120,0.35) 48%, transparent 60%),
      linear-gradient(to right, rgba(90,74,58,0.9) 0%, transparent 12%, transparent 100%),
      linear-gradient(to bottom, transparent 0%, transparent 52%, var(--crowd) 64%, var(--ground) 80%, var(--night-deep) 100%),
      linear-gradient(135deg, var(--haze) 0%, var(--night-mid) 38%, var(--night-deep) 75%);
  }
  .house-photo {
    position: absolute; left: 28px; top: 18px; right: 18px; bottom: 20px;
    background:
      linear-gradient(to bottom, transparent 0%, transparent 66%, rgba(20,28,6,0.85) 76%, #141a06 100%),
      linear-gradient(to right, transparent 0%, transparent 80%, rgba(20,30,6,0.75) 100%),
      radial-gradient(ellipse 38% 32% at 22% 20%, var(--glow-pale) 0%, rgba(238,249,210,0.4) 60%, transparent 100%),
      radial-gradient(ellipse 40% 35% at 55% 50%, var(--glow-green) 0%, rgba(156,216,56,0.3) 70%, transparent 100%),
      linear-gradient(to bottom, #b6e070 0%, var(--glow-mid) 55%, var(--glow-deep) 100%);
    box-shadow: inset 0 0 40px 18px var(--sleeve);
  }

  .artist, .title {
    position: absolute;
    font-family: "Cormorant Garamond", serif;
    font-weight: 300;
    color: var(--type);
    white-space: nowrap;
    line-height: 1;
  }
  .cover--festival .artist { right: 28px; top: 30px; font-size: 46px; letter-spacing: 7px; }
  .cover--festival .title { left: 78px; bottom: 30px; font-size: 46px; letter-spacing: 11px; }
  .cover--house .artist { right: 40px; bottom: 26px; font-size: 46px; letter-spacing: 7px; }

  .reflection {
    position: absolute; overflow: hidden;
    background: linear-gradient(to bottom, var(--reflect) 0%, #d8d8d8 45%, var(--page) 100%);
  }
  .reflection--festival { left: 30px; top: 813px; width: 550px; height: 87px; }
  .reflection--house { left: 624px; top: 810px; width: 552px; height: 90px; }
  .reflection .mirror {
    position: absolute;
    font-family: "Cormorant Garamond", serif;
    font-weight: 300;
    line-height: 1;
    color: #e2e2e2;
    transform: scaleY(-1);
    white-space: nowrap;
  }
  .reflection--festival .mirror { left: 78px; top: 22px; font-size: 46px; letter-spacing: 11px; }
  .reflection--house .mirror { right: 40px; top: 20px; font-size: 46px; letter-spacing: 7px; color: #a8a8a8; }
</style>
</head>
<body>
<main class="stage">
  <section class="cover cover--festival">
    <div class="festival-photo" role="img" aria-label="Night street festival with a balloon seller, crowds and lit garlands under streetlamps"></div>
    <p class="artist">kestrin</p>
    <p class="title">lo find quiet</p>
  </section>
  <div class="reflection reflection--festival" aria-hidden="true"><span class="mirror">lo find quiet</span></div>

  <section class="cover cover--house">
    <div class="house-photo" role="img" aria-label="Green-tinted old gabled house behind bare trees with an END road sign"></div>
    <p class="artist">kestrin</p>
  </section>
  <div class="reflection reflection--house" aria-hidden="true"><span class="mirror">kestrin</span></div>
</main>
</body>
</html>
```